Business Card Design

We are starting up a new Family run Business mainly offering a Free House Clearance service. We also offer the following chargeable services which include a Removals Service, Delivery and Collection of Items sold or purchased on Bidloft, Swapwren etc, including Motorcycles, Piano's, Furniture, Electrical appliances.
As there are a few Companies offering similar services we need to stand out and show what we do at a glance while appearing Professional and approachable
Updates

TidyNests

i  am liking some of the colours and designs so far but would like to see a few of our services listed as 1 or 2 have already done if this is possible and maybe some emphasis on the FREE House Clearance. thank you 
best regards
derek

Target Market(s)

Commercial and Domestic Tenants and Landlords aswell as Families looking for a friendly sympathetic clearance service after bereavement

Industry/Entity Type

Business

Contact Information for Business Card

TidyNests,
HouseClearance and Removals,
Marlow Dene
LM47 2QT
Tel: 07815239604
Email: enquiries@tidynests-example.info

```html
<!DOCTYPE html>
<html lang="en">
<head>
<meta charset="utf-8">
<title>Tidy Nests – Business Card</title>
<link href="https://fonts.googleapis.com/css2?family=Montserrat:wght@600&family=Lato:wght@400;700&display=swap" rel="stylesheet">
<style>
  :root {
    --backdrop: #d9dadb;
    --card: #0c0d0e;
    --white: #f4f4f4;
    --blue: #2aa6e0;
  }
  * { margin: 0; padding: 0; box-sizing: border-box; }
  html, body {
    width: 1200px;
    height: 926px;
    overflow: hidden;
    background: var(--backdrop);
  }
  .sheet {
    width: 1200px;
    height: 926px;
    display: flex;
    flex-direction: column;
    align-items: center;
    justify-content: center;
    gap: 46px;
  }
  .card {
    position: relative;
    width: 700px;
    height: 400px;
    background: var(--card);
    box-shadow: 0 6px 18px rgba(0,0,0,0.18);
  }
  .card-back {
    display: flex;
    align-items: center;
    justify-content: center;
  }
  .offer {
    font-family: "Lato", sans-serif;
    font-weight: 700;
    font-size: 36px;
    color: var(--blue);
    letter-spacing: 0.5px;
  }
  .brand {
    position: absolute;
    left: 40px;
    top: 138px;
    font-family: "Montserrat", sans-serif;
    font-weight: 600;
    font-size: 26px;
    letter-spacing: 3.5px;
    color: var(--white);
    text-transform: uppercase;
  }
  .services {
    position: absolute;
    right: 40px;
    top: 168px;
    font-family: "Lato", sans-serif;
    font-weight: 400;
    font-size: 19px;
    letter-spacing: 1.2px;
    color: var(--white);
  }
  .rule {
    position: absolute;
    left: 36px;
    right: 36px;
    top: 202px;
    height: 2px;
    background: var(--blue);
  }
  .contact {
    position: absolute;
    left: 40px;
    right: 40px;
    top: 220px;
    display: flex;
    justify-content: space-between;
    font-family: "Lato", sans-serif;
    font-size: 14.5px;
    letter-spacing: 0.6px;
    color: var(--blue);
  }
  .contact .sep { opacity: 0.9; }
</style>
</head>
<body>
  <main class="sheet">
    <section class="card card-back">
      <p class="offer">FREE House Clearance</p>
    </section>
    <section class="card card-front">
      <h1 class="brand">Tidy Nests</h1>
      <p class="services">House Clearance and Removals</p>
      <div class="rule"></div>
      <p class="contact">
        <span class="address">Marlow Dene LM47 2QT</span>
        <span class="sep">|</span>
        <span class="phone">T: 07815239604</span>
        <span class="sep">|</span>
        <span class="email">E: enquiries@tidynests-example.info</span>
      </p>
    </section>
  </main>
</body>
</html>
```